LEAP GLOW SWAY II (POSTCARD DESIGN)

Hello our original designer is no longer on this platform. We want to use design #51937604 with some minor adjustments. I've uploaded the original project 1) change the date on the front of card (keeping the same format) to August 27 with a start time of 2:30 PM.
2) on the front part of the card I want to include a splash graphic that says Back By Popular Demand! 3) replace pictures on the front with the attached photo. make it blend in. 3) Use the same photo on the back of the card.
Let the post card examples serve as template examples and let your creativity flourish! This is time sensitive so get these to me fast! If you're early you may win. thx

```html
<!DOCTYPE html>
<html lang="en">
<head>
<meta charset="utf-8">
<title>LEAP GLOW SWAY II – Postcard</title>
<link href="https://fonts.googleapis.com/css2?family=Poppins:ital,wght@0,300;0,400;0,600;0,800;1,800&family=Oswald:wght@500;600&family=Montserrat:wght@600;700&display=swap" rel="stylesheet">
<style>
  :root{
    --ink:#0b0b0d;
    --magenta:#d0107a;
    --pink-text:#e0157f;
    --blue:#1050c0;
    --cyan:#1aa0d0;
    --violet:#8a3fa8;
    --white:#ffffff;
    --navy:#1a3a9a;
    --page:#ffffff;
  }
  *{box-sizing:border-box;margin:0;padding:0}
  html,body{width:736px;height:1200px;overflow:hidden;background:var(--page)}
  body{position:relative;font-family:'Poppins',sans-serif}

  .card{position:absolute;left:48px;width:640px;height:425px;background:var(--ink);overflow:hidden;box-shadow:0 6px 18px rgba(0,0,0,.25)}
  .card--front{top:150px}
  .card--back{top:650px}
  .stripes{position:absolute;inset:0;width:100%;height:100%}

  .photo{position:absolute}
  .photo--dancer-veil{left:0;top:20px;width:178px;height:375px;
    background:linear-gradient(160deg,#7a4fc0 0%,#e9e6ee 35%,#f4f2f5 70%,#2a2a2e 100%);
    border-radius:40px 40px 10px 10px}
  .photo--host{right:0;top:45px;width:172px;height:380px;
    background:linear-gradient(180deg,#2b1d18 0%,#f1eeea 32%,#ece8e4 65%,#aebccf 100%);
    border-radius:70px 70px 0 0}
  .photo--dancer-sequin{left:360px;top:28px;width:240px;height:319px;
    background:linear-gradient(180deg,#1e1412 0%,#3a1f3c 35%,#4a2a50 70%,#3b2540 100%);
    border-radius:90px 90px 0 0}

  .kicker{color:var(--pink-text);font-weight:300;font-size:11px;line-height:16px;text-transform:uppercase;letter-spacing:.2px}
  .title{color:var(--white);font-weight:800;font-style:italic;line-height:.95}
  .title__line{display:block;font-size:52px}
  .title__line--big{font-size:78px;padding-right:8px;
    background:linear-gradient(90deg,var(--blue) 0%,var(--cyan) 35%,var(--violet) 70%,var(--magenta) 100%);
    -webkit-background-clip:text;background-clip:text;color:transparent}

  .front-copy{position:absolute;left:175px;width:300px;top:30px;text-align:center}
  .front-copy .title{margin-top:12px}
  .front-copy .title__line--big{display:inline-block}

  .splash{position:absolute;left:28px;top:272px;width:112px;height:112px;transform:rotate(-12deg)}
  .splash__burst{position:absolute;inset:0;width:100%;height:100%}
  .splash__text{position:absolute;inset:0;display:flex;flex-direction:column;align-items:center;justify-content:center;
    color:var(--white);font-weight:800;font-style:italic;text-transform:uppercase;text-align:center;line-height:1.05}
  .splash__small{font-size:10px;letter-spacing:.5px}
  .splash__big{font-size:14px}

  .pills{position:absolute;top:265px;left:190px;display:flex;gap:12px}
  .pill{display:flex;align-items:center;height:34px;background:var(--white);border-radius:17px;padding:0 12px 0 3px;font-family:'Oswald',sans-serif;color:var(--ink)}
  .pill__icon{width:28px;height:28px;border-radius:50%;background:var(--magenta);display:flex;align-items:center;justify-content:center;margin-right:4px}
  .pill__day{font-size:30px;font-weight:600;color:var(--magenta);line-height:1}
  .pill__month{font-size:8px;line-height:9px;margin-left:3px;font-weight:500}
  .pill__month b{display:block;font-size:12px;font-weight:500}
  .pill__time{font-size:21px;font-weight:500}

  .venue{position:absolute;top:310px;left:180px;width:265px;height:22px;background:var(--white);
    clip-path:polygon(3% 0,100% 8%,97% 100%,0 90%);display:flex;align-items:center;justify-content:center;gap:6px;
    font-family:'Oswald',sans-serif;font-size:11px;font-weight:500;color:var(--ink);text-transform:uppercase}
  .box-office{position:absolute;top:345px;left:175px;width:300px;text-align:center;font-family:'Montserrat',sans-serif;font-weight:700;font-size:13px;color:var(--white);letter-spacing:.5px}
  .box-office__label{color:var(--pink-text)}
  .web{position:absolute;top:371px;left:175px;width:300px;text-align:center;font-family:'Montserrat',sans-serif;font-weight:600;font-size:10px;color:var(--white);letter-spacing:4px}

  .back-copy{position:absolute;left:28px;top:26px;width:330px}
  .back-copy .title{margin-top:10px}
  .back-copy .title__line--big{display:inline-block}
  .about{position:absolute;left:25px;top:258px;width:310px;color:var(--white);font-size:7.6px;line-height:10.6px;font-weight:400}
  .about__lead{color:var(--pink-text);text-transform:uppercase}

  .ticket-bar{position:absolute;left:0;bottom:0;width:100%;height:78px;background:var(--white);display:flex;align-items:center;padding:0 30px;gap:14px;font-family:'Montserrat',sans-serif;font-weight:700}
  .ticket-brand{display:flex;align-items:center;gap:5px;font-size:10px;color:var(--navy);font-weight:700}
  .ticket-brand__mark{width:20px;height:20px;background:var(--magenta)}
  .ticket-bar__phone{font-size:17px;color:var(--navy);letter-spacing:.5px}
  .ticket-bar__phone span{color:var(--pink-text)}
  .ticket-bar__rule{width:1px;height:26px;border-left:1px dashed var(--navy)}
  .ticket-bar__web{font-size:15px;color:var(--pink-text);font-weight:600}
</style>
</head>
<body>

<section class="card card--front" aria-label="Postcard front">
  <svg class="stripes" viewBox="0 0 640 425" aria-hidden="true">
    <polygon fill="var(--magenta)" points="30,0 70,0 0,58 0,25"/>
    <polygon fill="var(--magenta)" points="130,0 218,0 0,135 0,80"/>
    <polygon fill="var(--magenta)" points="422,0 505,0 640,95 640,140"/>
    <polygon fill="var(--magenta)" points="560,0 640,0 640,40"/>
  </svg>
  <div class="photo photo--dancer-veil" role="img" aria-label="Photo of a dancer in white with a flowing purple veil"></div>
  <div class="photo photo--host" role="img" aria-label="Portrait of the headliner in a white blazer and jeans"></div>

  <div class="front-copy">
    <p class="kicker">Brightfield Productions presents<br>Nola Jean Rivers's</p>
    <h1 class="title">
      <span class="title__line">LEAP</span>
      <span class="title__line">Glow</span>
      <span class="title__line title__line--big">SWAY</span>
    </h1>
  </div>

  <div class="splash">
    <svg class="splash__burst" viewBox="0 0 110 110" aria-hidden="true">
      <polygon fill="var(--magenta)" stroke="var(--white)" stroke-width="2" points="109,55 97.5,66.4 101.8,82 86.1,86.1 82,101.8 66.4,97.5 55,109 43.6,97.5 28,101.8 23.9,86.1 8.2,82 12.5,66.4 1,55 12.5,43.6 8.2,28 23.9,23.9 28,8.2 43.6,12.5 55,1 66.4,12.5 82,8.2 86.1,23.9 101.8,28 97.5,43.6"/>
    </svg>
    <p class="splash__text">
      <span class="splash__small">Back By</span>
      <span class="splash__big">Popular</span>
      <span class="splash__big">Demand!</span>
    </p>
  </div>

  <div class="pills">
    <div class="pill">
      <span class="pill__icon">
        <svg width="16" height="16" viewBox="0 0 16 16" aria-hidden="true"><rect x="1.5" y="3" width="13" height="11" rx="1.5" fill="none" stroke="#fff" stroke-width="1.4"/><line x1="1.5" y1="6.5" x2="14.5" y2="6.5" stroke="#fff" stroke-width="1.4"/><line x1="5" y1="1" x2="5" y2="4" stroke="#fff" stroke-width="1.4"/><line x1="11" y1="1" x2="11" y2="4" stroke="#fff" stroke-width="1.4"/></svg>
      </span>
      <span class="pill__day">27</span>
      <span class="pill__month">AUGUST<b>2022</b></span>
    </div>
    <div class="pill">
      <span class="pill__icon">
        <svg width="16" height="16" viewBox="0 0 16 16" aria-hidden="true"><circle cx="8" cy="8" r="6.5" fill="none" stroke="#fff" stroke-width="1.4"/><polyline points="8,4 8,8 11,10" fill="none" stroke="#fff" stroke-width="1.4"/></svg>
      </span>
      <span class="pill__time">2:30 PM</span>
    </div>
  </div>

  <div class="venue">
    <svg width="9" height="12" viewBox="0 0 10 13" aria-hidden="true"><path d="M5 0C2.2 0 0 2.2 0 5c0 3.5 5 8 5 8s5-4.5 5-8C10 2.2 7.8 0 5 0z" fill="var(--magenta)"/><circle cx="5" cy="5" r="2" fill="#fff"/></svg>
    Harbor Lane Theatre Oak Ridge, CA
  </div>
  <p class="box-office"><span class="box-office__label">BOX OFFICE</span> (555) 014-SHOW</p>
  <p class="web">www.tixlink.ws/kvrQ</p>
</section>

<section class="card card--back" aria-label="Postcard back">
  <svg class="stripes" viewBox="0 0 640 425" aria-hidden="true">
    <polygon fill="var(--magenta)" points="422,0 505,0 640,95 640,150"/>
    <polygon fill="var(--magenta)" points="560,0 640,0 640,45"/>
  </svg>
  <div class="photo photo--dancer-sequin" role="img" aria-label="Photo of the headliner dancing in a dark sequined top"></div>

  <div class="back-copy">
    <p class="kicker">Brightfield Productions presents<br>Nola Jean Rivers's</p>
    <h2 class="title">
      <span class="title__line">LEAP</span>
      <span class="title__line">Glow</span>
      <span class="title__line title__line--big">SWAY</span>
    </h2>
  </div>

  <p class="about"><span class="about__lead">Leap, Glow, Sway</span> showcases the dance styles of urban hip hop, ballet, modern jazz and much much more! Bay Area renowned dancer/choreographer NOLA JEAN RIVERS headlines this cast of dancers and will amaze you as she takes you on a journey through dance you'll never forget. Join us for an experience that will prove to delight and excite you!</p>

  <div class="ticket-bar">
    <span class="ticket-brand"><span class="ticket-brand__mark"></span>TixHub</span>
    <span class="ticket-bar__phone"><span>BOX OFFICE</span> (555) 014-SHOW</span>
    <span class="ticket-bar__rule"></span>
    <span class="ticket-bar__web">www.tixlink.ws/kvrQ</span>
  </div>
</section>

</body>
</html>
```